Website for a Party Bus charter business

Please prepare a site for a local party bus charter company names Fenwick Bus Company.
They hire a party bus, chatrer bus, boat hire and party trailer hire (place holder photos fine for these items).
I have included a wireframe design. This should be used, however creative licence is fully extended
Delivery of PSD is required and all fonts and source files
The client likes: http://www.tallpinoca.com.au/ but must not look completely the same.
Should use a gold (simualr to #D1CFA1) colour, even if just background.
Hi All, just wondering if anyone is working on this as I have not received any responses or questions?
Is there anything I can do to assist?
Thanks all for the great submissions. I will be sending these onto the client today. Will let you know the outcome as soon as I can
Business

```html
<!DOCTYPE html>
<html lang="en">
<head>
<meta charset="utf-8">
<title>Fenwick Bus Company</title>
<link href="https://fonts.googleapis.com/css2?family=Mulish:wght@400;600;700&display=swap" rel="stylesheet">
<style>
:root{
  --gold:#d1cfa1;
  --gold-text:#f4f2dc;
  --red:#c8000a;
  --red-dark:#b30008;
  --ink:#222;
  --body:#555;
  --muted:#888;
  --line:#e0e0e0;
  --band:#e9e9e9;
  --footer:#2b2b2b;
  --white:#fff;
}
*{margin:0;padding:0;box-sizing:border-box}
html,body{width:1200px;height:2609px;overflow:hidden}
body{position:relative;background:var(--white);font-family:"Mulish",sans-serif;color:var(--body)}
.abs{position:absolute}

/* header */
.site-header{left:0;top:0;width:1200px;height:52px;background:var(--white)}
.brand{left:52px;top:12px;display:flex;align-items:center;gap:14px}
.brand-dot{width:28px;height:28px;border-radius:50%;background:#4b4b6e}
.brand-name{font-size:19px;font-weight:600;color:var(--ink);letter-spacing:.3px}
.social-strip{left:540px;top:0;width:200px;height:52px;background:#f2f2f2;display:flex;align-items:center;justify-content:center;gap:8px}
.social-strip span{width:26px;height:26px;background:#8a8a8a;border-radius:3px}
.util-icons{left:748px;top:13px;display:flex;gap:20px}
.search{left:838px;top:12px;width:236px;height:28px;border:1px solid var(--line);font-size:12px;color:#aaa;padding:6px 10px}
.search svg{position:absolute;right:6px;top:5px}
.like-badge{left:1088px;top:17px;width:60px;height:18px;background:#eee;border:1px solid #ccc;border-radius:2px}

/* hero */
.hero{left:0;top:52px;width:1200px;height:325px;background:#ddd;overflow:hidden}
.hero-panel{position:absolute;top:0;height:325px}
.thumbs{left:0;top:377px;width:1200px;height:153px;display:flex}
.thumb{position:relative;width:200px;height:153px}
.thumb-label{position:absolute;left:0;bottom:0;width:100%;height:34px;background:rgba(20,20,20,.82);color:var(--gold-text);font-size:13px;font-weight:600;text-align:center;line-height:34px;letter-spacing:.3px}

/* services */
.section-title{font-size:17px;font-weight:600;color:var(--ink);letter-spacing:.2px}
.service{width:520px;height:126px}
.service-photo{position:absolute;left:0;top:0;width:176px;height:125px}
.service-name{position:absolute;left:188px;top:0;font-size:19px;color:var(--red);font-weight:400}
.service-text{position:absolute;left:188px;top:28px;width:330px;font-size:13.5px;line-height:17px;color:var(--body)}
.read-more{position:absolute;left:426px;top:98px;width:89px;height:28px;background:var(--gold);color:var(--white);font-size:10px;text-align:center;line-height:28px}

/* video */
.video{left:52px;top:1029px;width:1096px;height:394px;background:linear-gradient(180deg,#2a2420 0%,#1a1614 55%,#0c0b0a 100%)}
.video-controls{position:absolute;left:0;bottom:0;width:100%;height:32px;background:#000}

/* story */
.story-photo{left:52px;top:1510px;width:477px;height:316px;background:linear-gradient(180deg,#10121c 0%,#2c1e18 55%,#6a3a1c 80%,#1a1010 100%)}
.story-text{left:591px;top:1518px;width:560px;font-size:15px;line-height:25px;color:#444}
.story-text p{margin-bottom:23px}
.btn-red{background:var(--red);color:var(--white);text-align:center}
.book-btn{left:591px;top:1783px;width:150px;height:41px;font-size:13px;line-height:41px;font-weight:600}

/* tweets */
.tweets{left:0;top:1889px;width:1200px;height:295px;background:var(--band)}
.tweet{width:420px;height:70px}
.tweet-avatar{position:absolute;left:0;top:0;width:75px;height:68px}
.tweet-text{position:absolute;left:87px;top:0;width:330px;font-size:13px;line-height:17px;color:#555}
.more-tweets{left:979px;top:106px;width:115px;height:82px;background:var(--gold);color:var(--white);font-size:10px;font-weight:700;line-height:12px;padding:29px 0 0 24px}
.more-tweets svg{position:absolute;right:22px;top:30px}

/* footer columns */
.col-title{font-size:16px;font-weight:600;color:var(--ink);padding-bottom:9px;border-bottom:1px solid var(--line)}
.col-text{font-size:15px;line-height:19px;color:#444}
.post{position:absolute;left:0;width:310px;height:58px}
.post-thumb{position:absolute;left:0;top:0;width:64px;height:57px}
.post-text{position:absolute;left:73px;top:2px;font-size:13px;line-height:17px;color:#555}
.field{position:absolute;left:0;width:358px;height:29px;border:1px solid var(--line);font-size:12px;color:#999;padding:6px 9px}
.footer-btn{position:absolute;width:306px;height:51px;font-size:18px;line-height:51px}

/* bottom bar */
.bottom-bar{left:0;top:2505px;width:1200px;height:104px;background:var(--footer);color:#9a9a9a;font-size:13px}
.social-round{position:absolute;top:42px;width:33px;height:33px;border-radius:50%;background:#6e6e6e}
</style>
</head>
<body>

<header class="site-header abs">
  <div class="brand abs"><span class="brand-dot"></span><span class="brand-name">FENWICK BUS COMPANY</span></div>
  <nav class="social-strip abs" aria-label="Social links"><span></span><span></span><span></span><span></span><span></span></nav>
  <div class="util-icons abs">
    <svg width="26" height="26" viewBox="0 0 26 26" aria-label="Favourites"><path d="M13 23 L3 12 A6 6 0 0 1 13 6 A6 6 0 0 1 23 12 Z" fill="#c8000a"/></svg>
    <svg width="28" height="26" viewBox="0 0 28 26" aria-label="Home"><path d="M2 13 L14 2 L26 13 L22 13 L22 24 L17 24 L17 17 L11 17 L11 24 L6 24 L6 13 Z" fill="#444"/></svg>
  </div>
  <div class="search abs">Search
    <svg width="16" height="16" viewBox="0 0 16 16"><circle cx="6.5" cy="6.5" r="4.5" fill="none" stroke="#333" stroke-width="2"/><path d="M10 10 L14 14" stroke="#333" stroke-width="2.4"/></svg>
  </div>
  <div class="like-badge abs"></div>
</header>

<section class="hero abs" role="img" aria-label="Carousel of party bus, nightlife and charter coach photos">
  <div class="hero-panel" style="left:0;width:96px;background:linear-gradient(180deg,#5a4a44,#2a2220)"></div>
  <div class="hero-panel" style="left:96px;width:113px;background:linear-gradient(180deg,#3a2a3a,#6a4a6a)"></div>
  <div class="hero-panel" style="left:209px;width:154px;background:linear-gradient(180deg,#40444a,#c8ccd2)"></div>
  <div class="hero-panel" style="left:363px;width:474px;background:linear-gradient(160deg,#1a1040 0%,#4a1a8a 40%,#8a3ac8 65%,#2a1050 100%)"></div>
  <div class="hero-panel" style="left:837px;width:153px;background:linear-gradient(180deg,#6a5a62,#4a3a40)"></div>
  <div class="hero-panel" style="left:990px;width:111px;background:linear-gradient(180deg,#8a8a90,#5a5a60)"></div>
  <div class="hero-panel" style="left:1101px;width:99px;background:linear-gradient(180deg,#2a2a2a,#8a2020)"></div>
</section>

<nav class="thumbs abs" aria-label="Fleet">
  <div class="thumb" role="img" aria-label="Colourful painted party bus" style="background:linear-gradient(180deg,#9ab8d8,#c84a6a 55%,#4a8a3a)"><span class="thumb-label">PARTY BUS</span></div>
  <div class="thumb" role="img" aria-label="White charter coach" style="background:linear-gradient(180deg,#a8c4e0,#e8ecf0 55%,#6a6a6a)"><span class="thumb-label">CHARTER BUS</span></div>
  <div class="thumb" role="img" aria-label="Painted party trailer" style="background:linear-gradient(180deg,#2a8ab8,#d83a3a 55%,#3a3a3a)"><span class="thumb-label">PARTY TRAILOR</span></div>
  <div class="thumb" role="img" aria-label="Party boat on the water" style="background:linear-gradient(180deg,#c8d4e0,#e8e8e8 50%,#3a5a7a)"><span class="thumb-label">PARTY BOAT</span></div>
  <div class="thumb" role="img" aria-label="House bus parked by a home" style="background:linear-gradient(180deg,#b8c8d8,#e0e0e0 55%,#5a7a4a)"><span class="thumb-label">HOUSE BUS</span></div>
  <div class="thumb" role="img" aria-label="Smiling owner in a suit" style="background:linear-gradient(180deg,#d8dce0,#a8b8c8 60%,#4a5a7a)"><span class="thumb-label">WANT YOU OWN?</span></div>
</nav>

<h2 class="section-title abs" style="left:52px;top:590px">FENWICK BUS COMPANY</h2>

<article class="service abs" style="left:52px;top:643px">
  <div class="service-photo" role="img" aria-label="Party bus interior with neon lights" style="background:linear-gradient(135deg,#0a2a4a,#1a6aa8 50%,#0a1a2a)"></div>
  <h3 class="service-name">Party Bus</h3>
  <p class="service-text">Duis aute irure dolor in reprehenderit in voluptate velit esse cillum dolore eu fugiat nulla pariatur. Duis aute irure dolor in reprehenderit in voluptate.</p>
  <span class="read-more">READ MORE</span>
</article>
<article class="service abs" style="left:631px;top:643px">
  <div class="service-photo" role="img" aria-label="Red double-decker bus in the city" style="background:linear-gradient(180deg,#a8b8c8,#8a7a6a 50%,#b82020 75%,#4a4a4a)"></div>
  <h3 class="service-name">House Bus</h3>
  <p class="service-text">Duis aute irure dolor in reprehenderit in voluptate velit esse cillum dolore eu fugiat nulla pariatur. Duis aute irure dolor in reprehenderit in voluptate.</p>
  <span class="read-more">READ MORE</span>
</article>
<article class="service abs" style="left:52px;top:810px">
  <div class="service-photo" role="img" aria-label="White charter coach on the road" style="background:linear-gradient(180deg,#e8ecf0,#f4f4f4 50%,#6a6a6a)"></div>
  <h3 class="service-name">Charter Bus</h3>
  <p class="service-text">Duis aute irure dolor in reprehenderit in voluptate velit esse cillum dolore eu fugiat nulla pariatur. Duis aute irure dolor in reprehenderit in voluptate.</p>
  <span class="read-more">READ MORE</span>
</article>
<article class="service abs" style="left:631px;top:810px">
  <div class="service-photo" role="img" aria-label="Lit party boat at night" style="background:linear-gradient(180deg,#0a1a3a,#3a5a8a 50%,#0a1020)"></div>
  <h3 class="service-name">Party Boat</h3>
  <p class="service-text">Duis aute irure dolor in reprehenderit in voluptate velit esse cillum dolore eu fugiat nulla pariatur. Duis aute irure dolor in reprehenderit in voluptate.</p>
  <span class="read-more">READ MORE</span>
</article>

<section class="video abs" role="img" aria-label="Video of guests silhouetted on a boat at sunset">
  <svg class="abs" style="left:499px;top:155px" width="74" height="74" viewBox="0 0 74 74"><circle cx="37" cy="37" r="34" fill="rgba(0,0,0,.3)" stroke="#bbb" stroke-width="3"/><path d="M29 22 L53 37 L29 52 Z" fill="#bbb"/></svg>
  <div class="video-controls">
    <svg class="abs" style="left:6px;top:5px" width="22" height="22" viewBox="0 0 22 22"><circle cx="11" cy="11" r="9.5" fill="none" stroke="#ddd" stroke-width="2"/><path d="M8.5 6.5 L15.5 11 L8.5 15.5 Z" fill="#ddd"/></svg>
    <div class="abs" style="left:36px;top:13px;width:1000px;height:6px;background:#ddd"></div>
    <div class="abs" style="left:36px;top:13px;width:340px;height:6px;background:#888"></div>
    <svg class="abs" style="left:1048px;top:7px" width="20" height="18" viewBox="0 0 20 18"><path d="M2 6 L6 6 L11 2 L11 16 L6 12 L2 12 Z" fill="#ddd"/><path d="M14 5 Q17 9 14 13" stroke="#ddd" stroke-width="1.6" fill="none"/></svg>
    <svg class="abs" style="left:1072px;top:8px" width="16" height="16" viewBox="0 0 16 16" fill="none" stroke="#ddd" stroke-width="2"><path d="M1 5 V1 H5 M11 1 H15 V5 M15 11 V15 H11 M5 15 H1 V11"/></svg>
  </div>
</section>

<div class="story-photo abs" role="img" aria-label="Riverside at night with lit boats and city lights"></div>
<div class="story-text abs">
  <p>Lorem ipsum dolor sit amet Consectetur adipisicing elit, sed do eiusmod tempor incididunt ut labore et dolore magna aliqua. Ut enim ad minim veniam, quis nostrud exercitation ullamco laboris nisi ut aliquip.</p>
  <p>Duis aute irure dolor in reprehenderit in voluptate velit esse cillum dolore eu fugiat nulla pariatur.</p>
  <p>Excepteur sint occaecat cupidatat non proident, sunt in culpa qui officia deserunt mollit anim id est laborum.Lorem ipsum dolor sit amet aliquip..</p>
</div>
<a class="book-btn btn-red abs">BOOK IT NOW</a>

<section class="tweets abs">
  <h2 class="section-title abs" style="left:52px;top:28px;font-size:16px">LATEST TWEETS</h2>
  <div class="tweet abs" style="left:52px;top:81px">
    <div class="tweet-avatar" role="img" aria-label="Car photo" style="background:linear-gradient(180deg,#6a7a8a,#2a3a4a)"></div>
    <p class="tweet-text">Excepteur sint occaecat cupidatat non proident, sunt in culpa qui officia deserunt mollit anim id est laborum.</p>
  </div>
  <div class="tweet abs" style="left:529px;top:81px">
    <div class="tweet-avatar" role="img" aria-label="Profile photo" style="background:linear-gradient(180deg,#8a6a4a,#d8b89a)"></div>
    <p class="tweet-text">Excepteur sint occaecat cupidatat non proident, sunt in culpa qui officia deserunt mollit anim id est laborum.</p>
  </div>
  <div class="tweet abs" style="left:52px;top:179px">
    <div class="tweet-avatar" role="img" aria-label="Profile photo" style="background:linear-gradient(180deg,#e8e0d0,#d8b88a)"></div>
    <p class="tweet-text">Excepteur sint occaecat cupidatat non proident, sunt in culpa qui officia deserunt mollit anim id est laborum.</p>
  </div>
  <div class="tweet abs" style="left:529px;top:179px">
    <div class="tweet-avatar" role="img" aria-label="Profile photo" style="background:linear-gradient(180deg,#3a4a6a,#c8b8a8)"></div>
    <p class="tweet-text">Excepteur sint occaecat cupidatat non proident, sunt in culpa qui officia deserunt mollit anim id est laborum.</p>
  </div>
  <a class="more-tweets abs">MORE<br>TWEETS
    <svg width="12" height="22" viewBox="0 0 12 22"><path d="M2 2 L10 11 L2 20" stroke="#fff" stroke-width="2.4" fill="none"/></svg>
  </a>
</section>

<section class="abs" style="left:52px;top:2244px;width:310px">
  <h2 class="col-title">QUOTE &amp; BOOKING</h2>
  <div class="abs" role="img" aria-label="Party bus lit in blue at night" style="left:0;top:52px;width:105px;height:104px;background:linear-gradient(135deg,#0a0a2a,#2a4ac8 55%,#c83a8a)"></div>
  <p class="col-text abs" style="left:122px;top:58px;width:188px">Excepteur sint occaecat cupidatat non proident, sunt in culpa qui officia</p>
  <a class="footer-btn btn-red" style="left:0;top:177px">GET A QUOTE</a>
</section>

<section class="abs" style="left:421px;top:2244px;width:306px">
  <h2 class="col-title">LATEST POSTS</h2>
  <div class="post" style="top:52px">
    <div class="post-thumb" role="img" aria-label="Post photo" style="background:linear-gradient(180deg,#8ac8e8,#d8b89a)"></div>
    <p class="post-text">Excepteur sint occaecat cupidatat<br>non proident, sunt in culpa</p>
  </div>
  <div class="post" style="top:115px">
    <div class="post-thumb" role="img" aria-label="Post photo" style="background:linear-gradient(180deg,#a8c8e0,#c8a88a)"></div>
    <p class="post-text">Excepteur sint occaecat cupidatat<br>non proident, sunt in culpa</p>
  </div>
  <div class="post" style="top:179px">
    <div class="post-thumb" role="img" aria-label="Post photo" style="background:linear-gradient(180deg,#c8d8e8,#d8a83a 55%,#4a4a4a)"></div>
    <p class="post-text">Excepteur sint occaecat cupidatat<br>non proident, sunt in culpa</p>
  </div>
</section>

<section class="abs" style="left:790px;top:2244px;width:360px">
  <h2 class="col-title">JOIN OUR VIP CLUB</h2>
  <p class="abs" style="left:0;top:50px;width:358px;font-size:13px;line-height:17px;color:#555">Secrint occaecat cupidatat non proident, sunt in culpa cepteur sint occaecat cupidatat</p>
  <div class="field" style="top:104px">Name</div>
  <div class="field" style="top:139px">Email Address</div>
  <a class="footer-btn btn-red" style="left:1px;top:177px;width:357px">JOIN OUR VIP CLUB</a>
</section>

<footer class="bottom-bar abs">
  <p class="abs" style="left:52px;top:50px">All Rights Reserved. Copyrights @ 2014</p>
  <span class="social-round" style="left:905px"></span>
  <span class="social-round" style="left:946px"></span>
  <span class="social-round" style="left:987px"></span>
  <span class="social-round" style="left:1026px"></span>
  <p class="abs" style="left:1097px;top:50px">Privacy</p>
  <p class="abs" style="left:1174px;top:50px;font-size:11px;color:#666">XS</p>
</footer>

</body>
</html>
```